NEW Modern Sleek Business Card for VR Language Startup

Our startup is using VR to lead the next wave of world language education. We need a two-sided business card that introduces the larger organization (Quorvel Language Inc) and our contact info on one side and shows the product, Lumidrasca, on the other side.

Side 1 (contact info)= Quorvel Logo and Contact info (name, title, phone, email)

Side 2 (product)= Lumidrasc logo, text, and website
Text= Culturally Immersive Language Learning Games
Website= www.lumidrasc.example

Target Market(s)

Education, Technology

Contact Information for Business Card

Contact info will be updated upon approval of the design. For now, put this as a placeholder.

Perry Hollins
Founder & CEO
phollins@mailtrove.example
(555)-014-2736

Font styles to use
Other font styles liked:
• Gibson and Century Gothic are the brand fonts

Requirements
Nice to have
• I would love to see cohesion between the design and colors of the two logos. I have attached a few business card designs that I like, so you can get a feel for my preferred style.

```html
<!DOCTYPE html>
<html lang="en">
<head>
<meta charset="utf-8">
<title>Quorvel Language – Business Card</title>
<link href="https://fonts.googleapis.com/css2?family=Montserrat:wght@400;500;600;700&display=swap" rel="stylesheet">
<style>
  :root {
    --backdrop: #d3d4d3;
    --orange: #f28a3c;
    --red: #ec3a55;
    --magenta: #c2418e;
    --violet: #7a55b5;
    --sky: #4cc0e8;
    --aqua: #a9e3e6;
    --ink: #1c1c1e;
    --paper: #ffffff;
    --tagline: #e8304f;
    --web: #6fd0ea;
  }
  html, body {
    margin: 0;
    width: 1200px;
    height: 900px;
    overflow: hidden;
    background: var(--backdrop);
    font-family: "Montserrat", sans-serif;
  }
  .sheet {
    width: 1200px;
    height: 900px;
    display: flex;
    flex-direction: column;
    align-items: center;
    justify-content: center;
    gap: 50px;
  }
  .card {
    width: 600px;
    height: 343px;
    box-shadow: 0 6px 14px rgba(0,0,0,0.25);
    display: block;
  }
  .card text { font-family: "Montserrat", sans-serif; }
</style>
</head>
<body>
<main class="sheet">

  <!-- Product side -->
  <svg class="card card--product" viewBox="0 0 600 343" aria-label="Lumidrasc product card">
    <defs>
      <linearGradient id="productGradient" x1="0" y1="0" x2="0" y2="1">
        <stop offset="0" stop-color="#f28a3c"/>
        <stop offset="0.3" stop-color="#ec3a55"/>
        <stop offset="0.55" stop-color="#c2418e"/>
        <stop offset="0.75" stop-color="#9aa6dc"/>
        <stop offset="1" stop-color="#a9e3e6"/>
      </linearGradient>
    </defs>
    <rect class="product-backdrop" width="600" height="343" fill="url(#productGradient)" role="img" aria-label="Soft gradient field where a scattered square pixel pattern sits"/>
    <circle class="brand-dot" cx="168" cy="150" r="14" fill="var(--paper)"/>
    <text class="brand-name" x="192" y="164" font-size="42" font-weight="600" fill="var(--paper)">Lumidrasc</text>
    <text class="product-tagline" x="300" y="236" text-anchor="middle" font-size="17" font-weight="700" fill="var(--tagline)">Culturally Immersive Language Learning Games</text>
    <rect class="web-tab" x="185" y="303" width="230" height="40" fill="var(--ink)"/>
    <text class="web-address" x="300" y="329" text-anchor="middle" font-size="15" font-weight="500" letter-spacing="1" fill="var(--web)">www.lumidrasc.example</text>
  </svg>

  <!-- Contact side -->
  <svg class="card card--contact" viewBox="0 0 600 343" aria-label="Quorvel Language contact card">
    <defs>
      <linearGradient id="contactGradient" x1="0" y1="0" x2="0" y2="1">
        <stop offset="0" stop-color="#f28a3c"/>
        <stop offset="0.3" stop-color="#ec3a55"/>
        <stop offset="0.6" stop-color="#c2418e"/>
        <stop offset="0.8" stop-color="#7a55b5"/>
        <stop offset="1" stop-color="#4cc0e8"/>
      </linearGradient>
    </defs>
    <rect class="contact-paper" width="600" height="343" fill="var(--paper)"/>
    <polygon class="divider-stripe" points="300,0 310,0 440,343 430,343" fill="var(--ink)"/>
    <polygon class="contact-panel" points="310,0 600,0 600,343 440,343" fill="url(#contactGradient)"/>

    <g class="company-mark" fill="var(--ink)">
      <circle class="brand-dot" cx="52" cy="176" r="11" fill="var(--magenta)"/>
      <text class="brand-name" x="72" y="188" font-size="34" font-weight="600" letter-spacing="3">QUORVEL</text>
      <text class="brand-name brand-name--sub" x="74" y="214" font-size="14" font-weight="600" letter-spacing="7">LANGUAGE</text>
    </g>

    <g class="contact-details" fill="var(--paper)" text-anchor="end">
      <text class="contact-name" x="582" y="70" font-size="21" font-weight="700">Perry Hollins</text>
      <text class="contact-title" x="582" y="90" font-size="13" font-weight="400">Founder &amp; CEO</text>
      <line class="contact-rule" x1="554" y1="106" x2="582" y2="106" stroke="var(--paper)" stroke-width="1.5"/>
      <text class="contact-phone" x="566" y="140" font-size="11.5">(555)-014-2736</text>
      <text class="contact-email" x="566" y="160" font-size="11.5">phollins@mailtrove.example</text>
    </g>
    <path class="icon-phone" d="M573 130 q-2 3 0 6 l2 3 q2 3 5 2 l1-1 -3-3 -1 1 q-2-1-3-4 l1-1 -2-3z" fill="var(--paper)"/>
    <g class="icon-mail" fill="none" stroke="var(--paper)" stroke-width="1.2">
      <rect x="572" y="151" width="11" height="8"/>
      <path d="M572 151 l5.5 4.5 5.5-4.5"/>
    </g>
  </svg>

</main>
</body>
</html>
```